WordPress design (BRTK)

We need a wordpress design for an established auction and real estate company based in Viginia- "Don't Pause.... Propel!". The winning design will incorporate a professional color scheme with company logo in a clean layout.
Industry/Entity Type
Real Estate
Requirements
Must have
- Navigation:
- 1) Home
- 2) Services
- 3) Auctions
- 4) Gala Benefit
- 5) Appraisals
- 6) Past Successes
- 7) About BRTK
- 8) Contact us
- Colors will be those in the attached logo. design should be able to be developed in responsive theme. Wants a "very clean and professional and sharp" design. Site will have slideshow that is relatively small, not a large portion of the design. Please use stock real estate image.
- Footer will have attached logos and contact info for the client.
Nice to have
- A representative drop down menu will be nice to see.

```html
<!DOCTYPE html>
<html lang="en">
<head>
<meta charset="utf-8">
<title>BRTK — Auctions &amp; Real Estate</title>
<link href="https://fonts.googleapis.com/css2?family=Open+Sans:wght@400;600;700&family=Noto+Serif:wght@400;700&display=swap" rel="stylesheet">
<style>
:root{
  --ink:#3a3a3a;
  --text:#7a7a7a;
  --muted:#8a8a8a;
  --brown:#5b2116;
  --brown-dark:#3d140c;
  --brown-light:#7c3a28;
  --price:#7a4d2e;
  --title:#4a2618;
  --charcoal:#2b2828;
  --line:#d8d8d8;
  --white:#fff;
  --photo-sky:#c9d6de;
  --photo-grass:#5f8a36;
  --photo-brick:#7a4a3a;
}
*{box-sizing:border-box;margin:0;padding:0}
html,body{width:731px;height:1200px;overflow:hidden;background:var(--white)}
body{font-family:"Open Sans",Verdana,sans-serif;color:var(--text);font-size:9px;line-height:1.5}
.page{position:relative;width:731px;height:1200px;overflow:hidden;background:linear-gradient(#fff 0,#fff 96px,#efefef 140px,#fafafa 300px,#fff 305px)}
.abs{position:absolute}

/* header */
.header-band{left:151px;top:18px;width:580px;height:78px;background:linear-gradient(#3a3636,#1f1d1d)}
.brand{left:0;top:0;width:151px;height:96px;background:linear-gradient(#2e2a2a,#191717);display:flex;align-items:center;justify-content:center}
.brand-name{font-weight:700;font-size:28px;letter-spacing:4px;color:#e9e2d6}
.nav{left:168px;top:18px;width:557px;height:30px;background:linear-gradient(var(--brown-light),var(--brown-dark));clip-path:polygon(0 0,100% 0,calc(100% - 14px) 100%,14px 100%);display:flex;align-items:center;justify-content:center;white-space:nowrap}
.nav a{color:#f1e6de;font-weight:700;font-size:9px;text-decoration:none;margin:0 6.5px}
.nav a.current{color:#fff;text-shadow:0 0 4px rgba(255,255,255,.4)}

/* welcome */
.welcome{left:23px;top:110px;width:245px}
.welcome h1{font-weight:400;font-size:18px;color:var(--ink);margin-bottom:6px;white-space:nowrap}
.welcome p{font-size:9px;color:var(--text)}
.keys-art{left:166px;top:189px;width:100px;height:64px;border-radius:3px;background:linear-gradient(90deg,rgba(255,255,255,0),#e6e2de 30%,#cdbcae)}
.header-block{left:23px;top:205px;width:245px}
.header-block h2{font-weight:400;font-size:12.5px;color:var(--ink);margin-bottom:3px;white-space:nowrap}
.header-block p{width:140px;font-size:9px}

/* slider */
.slider{left:286px;top:73px;width:427px;height:201px;background:#fff;box-shadow:0 0 6px rgba(0,0,0,.25);padding:6px 5px}
.slide-photo{width:100%;height:100%;background:linear-gradient(var(--photo-sky) 0,#e5e9e6 30%,var(--photo-brick) 48%,#4f6e32 66%,var(--photo-grass) 100%)}
.slide-caption{left:5px;bottom:6px;width:417px;height:62px;background:rgba(0,0,0,.55);padding:8px 9px;color:#eee}
.slide-caption h3{font-weight:400;font-size:12.5px;color:#fff;margin-bottom:2px}
.slide-caption p{font-size:8.3px;line-height:1.45}
.pager{left:291px;top:281px;display:flex;gap:4px}
.pager span{width:14px;height:14px;border:1px solid #bbb;background:#f4f4f4;font-size:8px;line-height:12px;text-align:center;color:#666}
.pager span.on{background:#555;color:#fff;border-color:#555}
.arrows{left:655px;top:282px;width:58px;height:14px;border:1px solid #bbb;background:linear-gradient(#fff,#e2e2e2);display:flex}
.arrows span{flex:1;display:flex;align-items:center;justify-content:center}
.arrows span+span{border-left:1px solid #ccc}
.rule{left:12px;top:304px;width:707px;height:2px;background:linear-gradient(90deg,rgba(91,33,22,.1),var(--brown) 50%,rgba(91,33,22,.1))}

/* listings */
.listing{width:170px}
.listing h4{font-family:"Noto Serif",Georgia,serif;font-weight:700;font-size:10.5px;color:var(--title);white-space:nowrap}
.post h4{font-family:"Noto Serif",Georgia,serif;font-weight:400;font-size:10.5px;color:var(--title)}
.meta{display:flex;align-items:center;font-size:8px;color:var(--muted);margin-top:7px;white-space:nowrap}
.ico-cal{width:10px;height:8px;border:1px solid #999;border-top-width:3px;border-radius:1px;margin-right:7px}
.ico-com{width:10px;height:7px;background:#aaa;border-radius:1px;margin:0 7px 0 18px;position:relative}
.ico-com::after{content:"";position:absolute;left:2px;bottom:-3px;border:2px solid transparent;border-top-color:#aaa}
.thumb{position:relative;width:165px;height:84px;margin-top:12px;background:#fff;padding:4px;box-shadow:0 1px 5px rgba(0,0,0,.3);overflow:hidden}
.thumb .photo{width:100%;height:100%}
.photo-brick{background:linear-gradient(#e3e7ea 0,#c9d2d6 25%,#7b5142 42%,#5a6f3a 62%,#6b9a3c 100%)}
.photo-victorian{background:linear-gradient(#b9cfe6 0,#8fb0d3 30%,#4a4660 48%,#c9c3c4 70%,#9a8e86 100%)}
.photo-stone{background:linear-gradient(#a9bfd8 0,#d0d7dd 30%,#6b5f5a 50%,#8c5448 72%,#5f7e3d 100%)}
.ribbon{position:absolute;right:-16px;top:8px;width:62px;height:11px;transform:rotate(45deg);font-size:5.5px;font-weight:700;color:#fff;text-align:center;line-height:11px;letter-spacing:.5px}
.ribbon.reduced{background:#8e8a3a}
.ribbon.sold{background:#a5231e}
.ribbon.rented{background:#c0692a}
.specs{font-size:8px;color:var(--text);margin-top:10px;white-space:nowrap}
.price{font-family:"Noto Serif",Georgia,serif;font-size:14.5px;color:var(--price);margin-top:2px;white-space:nowrap}
.price b{font-size:10px;font-weight:700;color:var(--ink)}
.listing p{font-size:9px;margin-top:5px;line-height:1.55}
.list-rule{left:23px;top:836px;width:361px;height:1px;background:var(--line)}
.btn{display:inline-flex;align-items:center;height:16px;padding:0 11px 0 3px;border:1px solid #ccc;border-radius:8px;background:linear-gradient(#fff,#e6e6e6);font-size:8px;font-weight:700;color:#555;box-shadow:0 1px 2px rgba(0,0,0,.15);white-space:nowrap}
.btn i{width:11px;height:11px;border-radius:50%;background:#555;margin-right:9px;position:relative}
.btn i::after{content:"";position:absolute;left:4px;top:3px;border:2.5px solid transparent;border-left:3.5px solid #fff}

/* sidebar */
.search{left:396px;top:323px;width:311px;height:33px;background:linear-gradient(#fdfdfd,#e9e9e9);border:1px solid #ddd;display:flex;align-items:center;padding:0 6px}
.search label{font-size:10.5px;color:#555;margin-right:7px;white-space:nowrap}
.search .field{width:190px;height:17px;border:1px solid #ccc;background:#fff;box-shadow:inset 0 1px 2px rgba(0,0,0,.1)}
.search .go{margin-left:6px;width:28px;height:17px;background:var(--brown);border:1px solid #3b120a;color:#f3e0d6;font-size:10px;text-align:center;line-height:15px}
.tabs{left:396px;top:370px;display:flex;gap:4px}
.tabs span{height:19px;padding:0 7px;font-size:9px;font-weight:700;line-height:19px;background:var(--brown);color:#f1e1d7;white-space:nowrap}
.tabs span.active{background:#fff;color:var(--ink);border:1px solid #ccc;border-bottom:none}
.tab-panel{left:401px;top:391px;width:301px;height:514px;background:#fff;border:1px solid #cfcfcf;box-shadow:0 0 0 4px #f0f0f0}
.post{position:absolute;left:12px;width:278px}
.post .meta{margin-top:9px}
.post p{font-size:9px;margin-top:10px;line-height:1.6}
.read-more{position:absolute;left:12px;width:288px;height:8px;border-bottom:1px solid var(--line)}
.read-more span{position:absolute;right:0;top:0;width:60px;height:9px;background:linear-gradient(#eee,#ddd);clip-path:polygon(8px 0,100% 0,100% 100%,0 100%);font-size:6.5px;color:#777;text-align:center;line-height:9px}

/* about + partners */
.about-band{left:12px;top:925px;width:707px;height:231px;background:linear-gradient(#fff 0,#f3f3f3 60%,#dcdcdc 100%);border-top:4px solid var(--charcoal)}
.about{left:23px;top:942px;width:205px}
.about h2{font-weight:400;font-size:16.5px;color:var(--ink);margin-bottom:10px}
.about p{font-size:9px;color:#444;line-height:1.55;margin-bottom:12px}
.partners{left:331px;top:943px;width:389px;height:174px;background:#fff}
.badge{position:absolute;background:#dedede;border:1px solid #bdbdbd}
.badge.dark{background:#3c3c3c;border-color:#222}
.badge.round{border-radius:50%}

/* footer */
.footer{left:0;top:1162px;width:731px;height:38px;border-top:2px solid var(--brown);background:linear-gradient(#fff,#f2f2f2);display:flex;align-items:center;justify-content:space-between;padding:0 15px 0 27px;white-space:nowrap}
.footer small{font-size:7.5px;font-weight:700;color:#999}
.footer nav{font-size:8.5px;font-weight:700;color:#555}
.footer nav a{color:#555;text-decoration:none}
.footer nav em{font-style:normal;color:#aaa;margin:0 5px}
</style>
</head>
<body>
<div class="page">

  <!-- header -->
  <div class="abs header-band"></div>
  <div class="abs brand"><span class="brand-name">BRTK</span></div>
  <nav class="abs nav">
    <a class="current" href="#">Home</a><a href="#">Services</a><a href="#">Auctions</a><a href="#">Gala Benefit</a><a href="#">Appraisals</a><a href="#">Past Successes</a><a href="#">About BRTK</a><a href="#">Contact Us</a>
  </nav>

  <section class="abs welcome">
    <h1>Sample Welcome Text</h1>
    <p>This is a sample welcome message, you can edit me on the wp-control panel, under Theme Editor &gt; Welcome Message</p>
  </section>
  <div class="abs keys-art" role="img" aria-label="Photo of a hand passing house keys to another hand"></div>
  <div class="abs header-block">
    <h2>Sample Header Block Title</h2>
    <p>This is a sample header block message, edit this on admin panel, under Theme Editor &gt; Home Text Block</p>
  </div>

  <!-- slideshow -->
  <div class="abs slider">
    <div class="slide-photo" role="img" aria-label="Photo of a large red-brick house with a green lawn"></div>
    <div class="abs slide-caption">
      <h3>161-6150 Euismod Road</h3>
      <p>Hollister 19779 New Brunswick Duis dolor purus, varius sit amet adipiscing sed, adipiscing eu neque. Sed mauris ante, interdum vel porttitor ...</p>
    </div>
  </div>
  <div class="abs pager"><span>1</span><span>2</span><span class="on">3</span></div>
  <div class="abs arrows">
    <span><svg width="6" height="6" viewBox="0 0 6 6"><path d="M5 0L0 3l5 3z" fill="#333"/></svg></span>
    <span><svg width="6" height="6" viewBox="0 0 6 6"><path d="M1 0l5 3-5 3z" fill="#333"/></svg></span>
  </div>
  <div class="abs rule"></div>

  <!-- listings -->
  <article class="abs listing" style="left:23px;top:323px">
    <h4>9532 Nunc Av.</h4>
    <div class="meta"><span class="ico-cal"></span>August 3rd, 2009<span class="ico-com"></span>10</div>
    <div class="thumb"><div class="photo photo-brick" role="img" aria-label="Photo of a brick house on a lawn"></div><span class="ribbon reduced">REDUCED</span></div>
    <div class="specs">8 Bed, 4 Bath, 3,582 Sq Ft</div>
    <div class="price"><b>Price :</b> $900 / Month</div>
    <p>Wichita 76899 British Columbia Etiam lorem purus, sagittis id congue sed, ullamcorper in magna. Vestibulum ante ipsum primis in faucibus orci ...</p>
  </article>
  <article class="abs listing" style="left:204px;top:323px">
    <h4>Ap #527-3516 A, St.</h4>
    <div class="meta"><span class="ico-cal"></span>August 3rd, 2009<span class="ico-com"></span>0</div>
    <div class="thumb"><div class="photo photo-victorian" role="img" aria-label="Photo of a Victorian house with a porch"></div><span class="ribbon sold">SOLD</span></div>
    <div class="specs">2 Bed, 2 Bath, 1,582 Sq Ft</div>
    <div class="price"><b>Price :</b> $300 / Month</div>
    <p>Twin Falls 78826 DC Maecenas lobortis diam et ipsum egestas euismod. Proin tincidunt tempus odio, at rhoncus purus bibendum vel. Mauris ...</p>
  </article>
  <article class="abs listing" style="left:23px;top:580px">
    <h4>161-6150 Euismod Road</h4>
    <div class="meta"><span class="ico-cal"></span>August 3rd, 2009<span class="ico-com"></span>0</div>
    <div class="thumb"><div class="photo photo-brick" role="img" aria-label="Photo of a brick house on a lawn"></div><span class="ribbon rented">RENTED</span></div>
    <div class="specs">5 Bed, 2 Bath, 2,800 Sq Ft</div>
    <div class="price"><b>Price :</b> $600 / Month</div>
    <p>Hollister 19779 New Brunswick Duis dolor purus, varius sit amet adipiscing sed, adipiscing eu neque. Sed mauris ante, interdum vel porttitor ...</p>
  </article>
  <article class="abs listing" style="left:204px;top:580px">
    <h4>P.O. Box 260, 281 Auctor Av.</h4>
    <div class="meta"><span class="ico-cal"></span>August 3rd, 2009<span class="ico-com"></span>0</div>
    <div class="thumb"><div class="photo photo-stone" role="img" aria-label="Photo of a stone and brick family house"></div><span class="ribbon sold">SOLD</span></div>
    <div class="specs">3 Bed, 4 Bath, 2,582 Sq Ft</div>
    <div class="price"><b>Price :</b> $700 / Month</div>
    <p>Corona 12039 WA Lorem ipsum dolor sit amet, consectetur adipiscing elit. Quisque ultricies, leo a pretium auctor, mauris dolor vehicula lectus, ...</p>
  </article>
  <div class="abs list-rule"></div>
  <span class="abs btn" style="left:24px;top:846px"><i></i>View All</span>

  <!-- sidebar -->
  <div class="abs search"><label>Search Website</label><span class="field"></span><span class="go">GO</span></div>
  <div class="abs tabs"><span class="active">Latest Post</span><span>Real Estate Blog</span><span>Best Resources</span></div>
  <aside class="abs tab-panel">
    <div class="post" style="top:13px">
      <h4>9532 Nunc Av.</h4>
      <div class="meta"><span class="ico-cal"></span>August 3rd, 2009<span class="ico-com"></span>10 Comments</div>
      <p>Wichita 76899 British Columbia Etiam lorem purus, sagittis id congue sed, ullamcorper in magna. Vestibulum ante ipsum primis in faucibus orci ...</p>
    </div>
    <div class="read-more" style="top:113px"><span>Read More</span></div>
    <div class="post" style="top:130px">
      <h4>Ap #527-3516 A, St.</h4>
      <div class="meta"><span class="ico-cal"></span>August 3rd, 2009<span class="ico-com"></span>No Comments</div>
      <p>Twin Falls 78826 DC Maecenas lobortis diam et ipsum egestas euismod. Proin tincidunt tempus odio, at rhoncus purus bibendum vel. Mauris ...</p>
    </div>
    <div class="read-more" style="top:230px"><span>Read More</span></div>
    <div class="post" style="top:247px">
      <h4>161-6150 Euismod Road</h4>
      <div class="meta"><span class="ico-cal"></span>August 3rd, 2009<span class="ico-com"></span>No Comments</div>
      <p>Hollister 19779 New Brunswick Duis dolor purus, varius sit amet adipiscing sed, adipiscing eu neque. Sed mauris ante, interdum vel porttitor ...</p>
    </div>
    <div class="read-more" style="top:347px"><span>Read More</span></div>
    <div class="post" style="top:364px">
      <h4>P.O. Box 260, 281 Auctor Av.</h4>
      <div class="meta"><span class="ico-cal"></span>August 3rd, 2009<span class="ico-com"></span>No Comments</div>
      <p>Corona 12039 WA Lorem ipsum dolor sit amet, consectetur adipiscing elit. Quisque ultricies, leo a pretium auctor, mauris dolor vehicula lectus, ...</p>
    </div>
    <div class="read-more" style="top:464px"><span>Read More</span></div>
    <span class="btn" style="position:absolute;left:13px;top:486px"><i></i>View All</span>
  </aside>

  <!-- about + partners -->
  <div class="abs about-band"></div>
  <section class="abs about">
    <h2>About Us</h2>
    <p>Lorem ipsum dolor sit amet, consectetur adipiscing elit. Ut ullamcorper luctus augue non venenatis. Donec consequat accumsan sapien, a pharetra lorem consectetur quis. Praesent sed erat nulla. Pellentesque quis velit a risus laoreet luctus. Nulla nibh odio.</p>
    <span class="btn"><i></i>Read More</span>
  </section>
  <div class="abs partners" aria-label="Partner and association badges">
    <span class="badge" style="left:10px;top:12px;width:36px;height:32px"></span>
    <span class="badge dark" style="left:63px;top:14px;width:78px;height:28px"></span>
    <span class="badge round" style="left:155px;top:10px;width:40px;height:38px"></span>
    <span class="badge" style="left:216px;top:14px;width:78px;height:30px"></span>
    <span class="badge" style="left:320px;top:14px;width:54px;height:30px"></span>
    <span class="badge" style="left:9px;top:68px;width:78px;height:30px"></span>
    <span class="badge dark" style="left:107px;top:62px;width:42px;height:40px"></span>
    <span class="badge" style="left:176px;top:64px;width:76px;height:36px"></span>
    <span class="badge dark" style="left:285px;top:64px;width:85px;height:40px"></span>
    <span class="badge" style="left:80px;top:122px;width:54px;height:40px"></span>
    <span class="badge round" style="left:161px;top:117px;width:52px;height:48px"></span>
    <span class="badge" style="left:242px;top:124px;width:76px;height:34px"></span>
  </div>

  <!-- footer -->
  <footer class="abs footer">
    <small>© Realestate | All Rights Reserved</small>
    <nav><a href="#">Home</a><em>|</em><a href="#">Services</a><em>|</em><a href="#">Auctions</a><em>|</em><a href="#">Gala Benefit</a><em>|</em><a href="#">Appraisals</a><em>|</em><a href="#">Past Successes</a><em>|</em><a href="#">About BRTK</a><em>|</em><a href="#">Contact Us</a></nav>
  </footer>

</div>
</body>
</html>
```